Create a pouch design for a new sports supplement product

Dimensions are 235mm (width) x 335mm (length) x 110mm (gusset)
File 1 - Extension of design brief please read both briefs
File 2 - Is 2 potential pouches this is just to give you a better example of size the dimensions are for the pouch on the right. This picture is not to give you design ideas as I am not very keen on either of these designs.
We need a design to be printed onto the pouches of our whey protein product. The brand name is 'Stellar Fuelworks' and needs to be displayed on the packaging either just writing or a simple logo design. I am not the most creative person in the world but have put together a more detailed brief listing some of the key information that needs to be included on the pouch (See attachment) Please feel free if you have experience of this the sports supplement market or have different ideas then please feel free to explore them.
The pouch would either be printed straight onto the pouch, or possibly just a printed label (front & back) to be stuck onto the pouch. Please design either or both.
Open to different colour schemes. Design has to be modern looking and eye-catching.
Some key points;
High quality whey protein concentrate
All Natural
Soy free
Great tasting
Please google image search 'protein pouches' to see other designs if your not familiar with the sports supplement market.
Any questions feel free to ask.
Updates
Hi, Thanks for all your design! I am really busy at the moment so haven't had chance to give feedback and have a proper look through all the designs. I have extended the time frame to give myself chance to give proper feedback and see any changes needed. Expect feedback sunday at the latest, and I will be pick a design early next week.
Target Market(s)
Sports supplement market. Product is a whey protein shake
Industry/Entity Type
Nutrition
Look and feel
Each slider illustrates characteristics of the customer's brand and the style your logo design should communicate.

```html
<!DOCTYPE html>
<html lang="en">
<head>
<meta charset="utf-8">
<title>Stellar Fuelworks – Natural Whey Protein Pouch</title>
<link rel="stylesheet" href="https://fonts.googleapis.com/css2?family=Michroma&family=Arimo:wght@400;700&display=swap">
<style>
  :root {
    --page-bg: #ffffff;
    --brand-red: #c8202e;
    --band-red-light: #e23a45;
    --band-red-dark: #a5141f;
    --silver-light: #f2f2f2;
    --silver-mid: #b9b9b9;
    --silver-dark: #6e6e6e;
    --ink: #111111;
    --ink-soft: #4a4a4a;
    --white: #ffffff;
  }
  * { box-sizing: border-box; margin: 0; padding: 0; }
  html, body {
    width: 880px; height: 1200px; overflow: hidden;
    background: var(--page-bg);
  }
  .canvas { position: relative; width: 880px; height: 1200px; }
  .pouch {
    position: absolute; left: 50px; top: 40px;
    width: 780px; height: 1120px;
    border-radius: 10px;
    overflow: hidden;
  }
  .pouch-backdrop {
    position: absolute; inset: 0;
    background:
      radial-gradient(ellipse 42% 30% at 50% 38%, rgba(255,255,255,0.95), rgba(255,255,255,0) 70%),
      radial-gradient(ellipse 60% 45% at 50% 62%, rgba(60,60,60,0.35), rgba(60,60,60,0) 75%),
      linear-gradient(90deg, var(--silver-dark) 0%, var(--silver-mid) 22%, var(--silver-light) 50%, var(--silver-mid) 78%, var(--silver-dark) 100%);
  }
  .seal-band {
    position: absolute; left: 0; top: 0; width: 100%; height: 190px;
    background: linear-gradient(180deg, var(--band-red-light) 0%, var(--brand-red) 45%, rgba(200,32,46,0.55) 78%, rgba(200,32,46,0) 100%);
  }
  .tear-note {
    position: absolute; right: 46px; top: 100px;
    font: 400 13px/1 "Arimo", sans-serif;
    color: var(--white);
    display: flex; align-items: center; gap: 6px;
  }
  .tear-note svg { width: 10px; height: 12px; }
  .brand-name {
    position: absolute; left: 0; width: 100%; top: 300px;
    text-align: center;
    font-family: "Michroma", sans-serif;
    font-weight: 400;
    color: var(--brand-red);
    line-height: 1;
  }
  .brand-name .line-1 { display: block; font-size: 96px; letter-spacing: 2px; }
  .brand-name .line-2 { display: block; font-size: 62px; margin-top: 28px; letter-spacing: 1px; }
  .product-type {
    position: absolute; left: 0; width: 100%; top: 556px;
    text-align: center;
    font: 400 26px/1 "Arimo", sans-serif;
    color: var(--ink);
  }
  .flavour-badge {
    position: absolute; left: 225px; top: 752px;
    width: 330px; height: 66px;
    border-radius: 16px;
    background: linear-gradient(180deg, var(--band-red-light), var(--band-red-dark));
    color: var(--white);
    font: 400 27px/66px "Arimo", sans-serif;
    text-align: center;
  }
  .claims {
    position: absolute; left: 0; width: 100%; top: 858px;
    list-style: none; text-align: center;
    font: 700 19px/1 "Arimo", sans-serif;
    color: var(--ink);
  }
  .claims li { margin-bottom: 27px; }
  .net-weight {
    position: absolute; left: 0; width: 100%; top: 1060px;
    text-align: center;
    font: 400 16px/1 "Arimo", sans-serif;
    color: var(--ink-soft);
  }
</style>
</head>
<body>
  <main class="canvas">
    <section class="pouch">
      <div class="pouch-backdrop" role="img" aria-label="Soft silver gradient background with a blurred athlete photograph and halftone dots"></div>
      <div class="seal-band"></div>
      <p class="tear-note">Tear here and Reseal
        <svg viewBox="0 0 10 12" aria-hidden="true"><polygon points="0,0 10,6 0,12" fill="#f5b21c"/></svg>
      </p>
      <h1 class="brand-name">
        <span class="line-1">STELLAR</span>
        <span class="line-2">FUELWORKS</span>
      </h1>
      <p class="product-type">Natural Whey Protein</p>
      <p class="flavour-badge">Strawberry Flavour</p>
      <ul class="claims">
        <li>No artificial Flavours</li>
        <li>Excellent Amino acid profile</li>
        <li>80% high quality protein content</li>
        <li>Soy free</li>
      </ul>
      <p class="net-weight">909g 30 servings</p>
    </section>
  </main>
</body>
</html>
```